Ridgeline Build Network Inc. Letterhead

Creation of attractive and eye catching letterhead for a business start-up for the construction industry. Letterhead must relate to construction, but avoid standard hammer and tools in the design.

I forgot to add some details, sorry about that. Some pertinent info: Ph: 916-555-0187 ridgelinebuildnet.example 274 Marrowell Ave, Ste 300 Alderbrook, CA 95999 info@ridgelinebuildnet.example not sure if slogan should be in there" “Bringing building professionals together to shape a stronger trade.” must be able to be used in word. Thanks!

```html
<!DOCTYPE html>
<html lang="en">
<head>
<meta charset="utf-8">
<title>Ridgeline Build Network Inc. Letterhead</title>
<link href="https://fonts.googleapis.com/css2?family=Lato:wght@400;700;900&display=swap" rel="stylesheet">
<style>
  :root {
    --backdrop: #e4e4e4;
    --paper: #f1f1f1;
    --navy: #1e2452;
    --red: #b11f24;
    --ink: #555555;
    --ink-soft: #666666;
  }
  * { margin: 0; padding: 0; box-sizing: border-box; }
  html, body {
    width: 1200px;
    height: 1154px;
    overflow: hidden;
    background: var(--backdrop);
    font-family: "Lato", Arial, sans-serif;
  }
  .letterhead {
    position: absolute;
    left: 209px;
    top: 27px;
    width: 782px;
    height: 1100px;
    background: var(--paper);
    overflow: hidden;
  }
  .brand {
    position: absolute;
    left: 57px;
    top: 130px;
    width: 300px;
    color: var(--navy);
  }
  .brand-name {
    display: flex;
    align-items: center;
    gap: 9px;
    font-weight: 900;
    font-size: 20px;
    line-height: 1.1;
    color: var(--navy);
    white-space: nowrap;
  }
  .brand-mark {
    flex: 0 0 auto;
    width: 14px;
    height: 14px;
    background: var(--red);
  }
  .brand-slogan {
    margin-top: 10px;
    font-weight: 900;
    font-size: 9.5px;
    letter-spacing: 0.6px;
    color: var(--navy);
    white-space: nowrap;
  }
  .contact {
    position: absolute;
    left: 533px;
    top: 86px;
    font-size: 13px;
    font-style: normal;
    color: var(--ink-soft);
    line-height: 18.5px;
    white-space: nowrap;
  }
  .contact-address { margin-bottom: 8px; }
  .contact-row {
    display: flex;
    align-items: center;
    gap: 7px;
  }
  .contact-row svg { width: 13px; height: 13px; flex: 0 0 auto; }
  .mission {
    position: absolute;
    left: 0;
    top: 222px;
    width: 100%;
    display: flex;
    align-items: center;
  }
  .mission-rule {
    height: 1.5px;
    background: var(--red);
  }
  .mission-rule.left { width: 169px; }
  .mission-rule.right { flex: 1; }
  .mission-text {
    padding: 0 13px;
    font-size: 13.5px;
    color: var(--ink);
    white-space: nowrap;
  }
  .footer-line {
    position: absolute;
    left: 0;
    top: 1070px;
    width: 100%;
    height: 4px;
    background: var(--navy);
  }
  .footer-band {
    position: absolute;
    left: 0;
    top: 1077px;
    width: 100%;
    height: 23px;
    background: var(--red);
  }
</style>
</head>
<body>
  <main class="letterhead">
    <header>
      <div class="brand">
        <div class="brand-name"><span class="brand-mark"></span><span>Ridgeline Build Network</span></div>
        <div class="brand-slogan">PLAN. PARTNER. PROGRESS.</div>
      </div>

      <address class="contact">
        <div class="contact-address">274 Marrowell Ave<br>Ste 300 Alderbrook, CA 95999</div>
        <div class="contact-row">
          <svg viewBox="0 0 16 16" aria-hidden="true"><path d="M4 1.5c1 0 2 2.2 2 3 0 .9-1.3 1.2-1.3 2 0 1.4 3.4 4.8 4.8 4.8.8 0 1.1-1.3 2-1.3.8 0 3 1 3 2 0 1.2-1.6 2.5-3 2.5C6.5 14.5 1.5 9.5 1.5 4.5c0-1.4 1.3-3 2.5-3z" fill="#b11f24"/></svg>
          <span>916-555-0187</span>
        </div>
        <div class="contact-row">
          <svg viewBox="0 0 16 16" aria-hidden="true"><rect x="1" y="3" width="14" height="10" fill="#b11f24"/><path d="M1.5 3.5 8 9l6.5-5.5" stroke="#f1f1f1" stroke-width="1.3" fill="none"/></svg>
          <span>info@ridgelinebuildnet.example</span>
        </div>
        <div class="contact-row">
          <svg viewBox="0 0 16 16" aria-hidden="true"><circle cx="8" cy="8" r="6.5" fill="none" stroke="#b11f24" stroke-width="1.4"/><ellipse cx="8" cy="8" rx="2.8" ry="6.5" fill="none" stroke="#b11f24" stroke-width="1.2"/><path d="M1.5 8h13M2.5 5h11M2.5 11h11" stroke="#b11f24" stroke-width="1.1"/></svg>
          <span>www.ridgelinebuildnet.example</span>
        </div>
      </address>

      <div class="mission">
        <span class="mission-rule left"></span>
        <span class="mission-text">Bringing building professionals together to shape a stronger trade.</span>
        <span class="mission-rule right"></span>
      </div>
    </header>

    <footer>
      <div class="footer-line"></div>
      <div class="footer-band"></div>
    </footer>
  </main>
</body>
</html>
```